Learn-to-Swim Program for Children's Day Camp (Walter Brisbane Fieldgrounds)

We are a children's camp with a robust swim instruction program and we need a series of 5 kid-friendly banners which list the skills learned in our swim program that can be hung up around each outdoor pool complex. All together there are 6 overarching levels and 12 sublevels (see attached). Except for the Level V & VI, each banner should be one overarching level and the 2-3 sublevels that define it.

Each swim level has a name, most of which are sea creatures, and we want to have a corresponding image/avatar to go with the swim level name (e.g. tadpole, barracuda, orca, goldfish, catfish).

The banners should be 3 feet (width) by 5 feet (height). The banners will be hung outdoors so it needs a color scheme that won't get lost in the sunlight.

We will want to include our logo but do not need the design to match our logo colors. Logo can be in black or white.

Our website is: www.campwbf.org

Target Market(s)

children age 5 - 12

Industry/Entity Type

children's day camp

Requirements
Must have
• A progression from level I to level VI. Should have a happy, bright, fun, tone, text MUST be legible from at least a 5 foot distance
Should not have
• adult themes, a scheme that evokes sadness or fear

```html
<!DOCTYPE html>
<html lang="en">
<head>
<meta charset="utf-8">
<title>Learn-to-Swim Level Banners · Walter Brisbane Fieldgrounds</title>
<link rel="stylesheet" href="https://fonts.googleapis.com/css2?family=Rubik+Dirt&family=Happy+Monkey&family=Arimo:wght@400;700&family=Oswald:wght@600&display=swap">
<style>
  :root{
    --backdrop:#363636;
    --sand:#f8dcb5;
    --taupe:#7b6d5d;
    --earth:#4a3b2e;
    --ink:#111111;
    --silver:#d9d6d2;
    --illo-light:#a08670;
    --illo-dark:#3b3029;
  }
  *{box-sizing:border-box;margin:0;padding:0}
  html,body{width:1135px;height:1200px;overflow:hidden;background:var(--backdrop)}
  .canvas{position:relative;width:1135px;height:1200px;background:var(--backdrop)}

  .banner{position:absolute;width:298px;height:497px;background:var(--sand);overflow:hidden}
  .banner-shapes{position:absolute;inset:0;width:298px;height:497px}

  .camp-name{position:absolute;top:20px;left:60px;width:150px;display:flex;align-items:center;justify-content:center;gap:4px;
    font-family:"Arimo",Arial,sans-serif;font-weight:700;font-size:6.3px;letter-spacing:.2px;color:var(--ink);text-transform:uppercase}
  .camp-name .mark{width:9px;height:9px;background:var(--ink)}

  .level-title{position:absolute;font-family:"Rubik Dirt",Impact,sans-serif;font-size:19px;line-height:1;letter-spacing:1px;
    color:var(--ink);padding-bottom:3px;border-bottom:2px solid var(--ink)}

  .skills{position:absolute;list-style:none;font-family:"Happy Monkey",cursive;font-size:8.4px;line-height:10.2px;color:var(--ink)}
  .skills li{position:relative;padding-left:18px;margin-bottom:1px}
  .skills.roomy li{margin-bottom:3.6px}
  .skills li::before{content:"";position:absolute;left:0;top:2px;width:6px;height:6px;border:1px solid var(--ink);border-radius:50%}
  .skills li::after{content:"";position:absolute;left:2px;top:4.2px;width:2px;height:2px;border-top:1px solid var(--ink);border-right:1px solid var(--ink);transform:rotate(45deg)}

  .move-up{position:absolute;display:flex;align-items:flex-start;gap:12px;font-family:"Arimo",Arial,sans-serif;font-weight:700;font-size:8.6px;line-height:10.4px;color:var(--ink)}
  .move-up.stacked{flex-direction:column;gap:4px;font-size:6.3px;line-height:7.4px}
  .move-up-tag{flex:none;width:30px;height:13px;background:var(--ink);color:#fff;font-family:"Oswald",sans-serif;font-weight:600;font-size:5.6px;
    line-height:13px;padding-left:3px;clip-path:polygon(0 0,72% 0,72% 0,100% 50%,72% 100%,0 100%)}

  .illo{position:absolute;border-radius:40%;background:radial-gradient(ellipse at 40% 40%,var(--illo-light),var(--illo-dark))}
</style>
</head>
<body>
<main class="canvas">

  <!-- Banner 1: Wader & Splasher -->
  <section class="banner" style="left:100px;top:101px">
    <svg class="banner-shapes" viewBox="0 0 298 497" aria-hidden="true">
      <path d="M0,0H298V8C220,72 80,78 0,6Z" fill="var(--taupe)"/>
      <path d="M0,6C80,78 220,72 298,8" fill="none" stroke="var(--silver)" stroke-width="1.5"/>
      <path d="M0,282C120,276 220,240 298,204L298,250C220,290 110,302 0,308Z" fill="var(--taupe)"/>
      <path d="M0,282C120,276 220,240 298,204" fill="none" stroke="var(--earth)" stroke-width="3"/>
      <path d="M0,308C110,302 220,290 298,250" fill="none" stroke="var(--silver)" stroke-width="1.5"/>
      <path d="M85,497C130,482 200,480 250,497Z" fill="var(--taupe)"/>
    </svg>
    <div class="camp-name"><span class="mark"></span>Walter Brisbane Fieldgrounds</div>

    <h2 class="level-title" style="left:18px;top:74px">WADER</h2>
    <div class="illo" role="img" aria-label="Illustration of a wading heron standing on a rock" style="left:206px;top:68px;width:75px;height:124px"></div>
    <ul class="skills roomy" style="left:26px;top:108px;width:170px">
      <li>Gets into the water with assistance</li>
      <li>Follows pool rules</li>
      <li>Can hold big breath and get chin/ cheeks in water</li>
      <li>Cups hands to hold water and get some of face wet</li>
      <li>Doesn't always need assistance in water</li>
    </ul>
    <div class="move-up" style="left:24px;top:234px"><span class="move-up-tag">Move-Up</span><span>Must be comfortable<br>entering the water</span></div>

    <h2 class="level-title" style="left:18px;top:323px">SPLASHER</h2>
    <div class="illo" role="img" aria-label="Illustration of a child swimming butterfly with big splashes" style="left:139px;top:296px;width:151px;height:56px"></div>
    <ul class="skills" style="left:26px;top:359px;width:190px;line-height:10.4px">
      <li style="margin-bottom:3px">Enters and exits pool without assistance</li>
      <li style="margin-bottom:3px">Can do a slide in entry</li>
      <li style="margin-bottom:3px">Plays in water up to chest deep</li>
      <li>Dips face and head in water</li>
    </ul>
    <div class="move-up" style="left:24px;top:438px"><span class="move-up-tag">Move-Up</span><span>Must fully submerge body and head<br>underwater (no nose holding)</span></div>
  </section>

  <!-- Banner 2: Guppy & Tadpole -->
  <section class="banner" style="left:419px;top:101px">
    <svg class="banner-shapes" viewBox="0 0 298 497" aria-hidden="true">
      <path d="M0,0H298V8C220,70 80,76 0,6Z" fill="var(--taupe)"/>
      <path d="M0,6C80,76 220,70 298,8" fill="none" stroke="var(--silver)" stroke-width="1.5"/>
      <path d="M0,255C100,268 200,248 298,212L298,255C220,268 100,290 0,316Z" fill="var(--taupe)"/>
      <path d="M0,255C100,268 200,248 298,212" fill="none" stroke="var(--silver)" stroke-width="1.5"/>
      <path d="M0,316C100,290 220,268 298,255" fill="none" stroke="var(--earth)" stroke-width="2"/>
      <path d="M85,497C130,482 200,480 250,497Z" fill="var(--taupe)"/>
    </svg>
    <div class="camp-name"><span class="mark"></span>Walter Brisbane Fieldgrounds</div>

    <h2 class="level-title" style="left:18px;top:69px">GUPPY</h2>
    <div class="illo" role="img" aria-label="Illustration of a guppy with a flowing fan tail" style="left:196px;top:52px;width:90px;height:74px"></div>
    <ul class="skills" style="left:30px;top:99px;width:230px">
      <li style="width:170px">Fully submerges and retrieves object from under water</li>
      <li>Blows bubbles through nose and mouth</li>
      <li>Floats on stomach with support (10 seconds) Floats on back with support (10 seconds)</li>
      <li>Assisted glide on stomach- no kicking</li>
      <li>Rolls from front to back and back to front with support</li>
      <li>Straight leg flutter kick on front and back (15 seconds) with support</li>
    </ul>
    <div class="move-up" style="left:26px;top:215px"><span class="move-up-tag">Move-Up</span><span>Must demonstrate straight flutter<br>kicks and float with support</span></div>

    <h2 class="level-title" style="left:41px;top:300px">TADPOLE</h2>
    <div class="illo" role="img" aria-label="Illustration of a tadpole with tiny legs and a long tail" style="left:192px;top:265px;width:85px;height:62px"></div>
    <ul class="skills" style="left:30px;top:330px;width:250px">
      <li>Floats on back unsupported (10 sec)</li>
      <li>Floats on stomach unsupported (10 sec)</li>
      <li>Launch glide on stomach with proper flutter kick unassisted</li>
      <li>Launch glide on back with proper flutter kick unassisted</li>
      <li>Push off and swim using combination of arm and leg actions for 10 feet on front and back</li>
      <li>Launch-roll to back float unsupported</li>
      <li>Jump in and float on the back</li>
    </ul>
    <div class="move-up" style="left:26px;top:448px"><span class="move-up-tag">Move-Up</span><span>Must perform proper flutter kicks and glides<br>unsupported. Must jump in and float<br>on the back for 10 sec.</span></div>
  </section>

  <!-- Banner 3: Minnow, Goldfish & Catfish -->
  <section class="banner" style="left:737px;top:101px">
    <svg class="banner-shapes" viewBox="0 0 298 497" aria-hidden="true">
      <path d="M0,0H298V8C220,68 80,74 0,6Z" fill="var(--taupe)"/>
      <path d="M0,6C80,74 220,68 298,8" fill="none" stroke="var(--silver)" stroke-width="1.5"/>
      <path d="M0,190C100,186 210,206 298,236L298,242C210,212 100,192 0,196Z" fill="var(--taupe)"/>
      <path d="M0,196C100,192 210,212 298,242" fill="none" stroke="#ffffff" stroke-width="1.5"/>
      <path d="M0,336C100,328 200,326 298,332L298,345C260,338 230,336 200,336C120,334 60,338 0,340Z" fill="var(--taupe)"/>
      <path d="M0,340C60,338 120,334 200,336" fill="none" stroke="#ffffff" stroke-width="1.2"/>
      <path d="M220,497C250,487 275,482 298,479V497Z" fill="var(--taupe)"/>
    </svg>
    <div class="camp-name"><span class="mark"></span>Walter Brisbane Fieldgrounds</div>

    <h2 class="level-title" style="left:18px;top:61px">MINNOW</h2>
    <div class="illo" role="img" aria-label="Illustration of a small minnow" style="left:213px;top:49px;width:85px;height:28px"></div>
    <ul class="skills" style="left:26px;top:86px;width:272px;line-height:9.2px">
      <li>Proper streamline body position (on back and stomach) with flutter kick</li>
      <li>Kick on stomach, arms to side, roll to back float, big breath in, back to kick on stomach</li>
      <li>Correct front crawl arm motion with side breathing</li>
      <li>Can exit pool independently (elbows and knees)</li>
      <li style="width:170px">Correct backstroke arm motion</li>
      <li style="width:170px">Demonstrate basic front crawl</li>
      <li style="width:170px">Demonstrate basic backstroke</li>
    </ul>
    <div class="move-up stacked" style="left:216px;top:146px;width:80px"><span class="move-up-tag">Move-Up</span><span>Must perform basic front crawl and backstroke. Must jump into deep water, float and kick to the side of the pool independently</span></div>

    <h2 class="level-title" style="left:18px;top:200px">GOLDFISH</h2>
    <div class="illo" role="img" aria-label="Illustration of a smiling goldfish" style="left:207px;top:247px;width:79px;height:44px"></div>
    <ul class="skills" style="left:26px;top:226px;width:240px;line-height:9.4px">
      <li style="width:170px">One arm up one arm down on stomach then to back</li>
      <li>Streamline on front roll to streamline on back</li>
      <li>Basic rhythmic breathing</li>
      <li>Demonstrates proper front crawl</li>
      <li>Demonstrates proper backstroke</li>
      <li>Treading 1 minute</li>
      <li>Basic elementary backstroke</li>
      <li>Side flutter kick</li>
      <li>Streamline roll to side kick</li>
    </ul>
    <div class="move-up stacked" style="left:189px;top:289px;width:100px"><span class="move-up-tag">Move-Up</span><span>Must complete deep water orientation, front crawl, and backstroke with stamina</span></div>

    <h2 class="level-title" style="left:18px;top:344px">CATFISH</h2>
    <div class="illo" role="img" aria-label="Illustration of a catfish with whiskers" style="left:201px;top:349px;width:97px;height:28px"></div>
    <ul class="skills" style="left:26px;top:370px;width:272px;line-height:9.4px">
      <li>Tread water for 2 min continuously</li>
      <li>Front crawl with rhythmic breathing, fingertip</li>
      <li>Entry, arm reach and body roll consistent and with stamina</li>
      <li style="width:180px">Catch-up stroke with alternate breathing every 3 counts</li>
      <li style="width:180px">Front crawl with alternate breathing and side flutter kick</li>
      <li>Double arm backstroke with pull</li>
      <li>Backstroke switch</li>
      <li>Sitting and kneeling dives with streamline position</li>
    </ul>
    <div class="move-up stacked" style="left:212px;top:400px;width:84px"><span class="move-up-tag">Move-Up</span><span>Must perform advanced front crawl with fingertip entry and rhythmic breathing consistently and with stamina</span></div>
  </section>

  <!-- Banner 4: Dolphin, Marlin & Barracuda -->
  <section class="banner" style="left:269px;top:621px">
    <svg class="banner-shapes" viewBox="0 0 298 497" aria-hidden="true">
      <path d="M0,0H298V8C220,68 80,74 0,6Z" fill="var(--taupe)"/>
      <path d="M0,6C80,74 220,68 298,8" fill="none" stroke="var(--silver)" stroke-width="1.5"/>
      <path d="M0,214C100,212 210,200 290,188L298,188V198C210,214 100,226 0,226Z" fill="var(--taupe)"/>
      <path d="M0,224C100,222 210,212 298,196" fill="none" stroke="var(--earth)" stroke-width="3"/>
      <path d="M0,214C100,212 210,200 290,188" fill="none" stroke="#ffffff" stroke-width="1.2"/>
      <path d="M0,370C100,362 200,362 298,368L298,376C200,370 100,370 0,378Z" fill="var(--earth)"/>
      <path d="M0,378C100,370 200,370 298,376" fill="none" stroke="#ffffff" stroke-width="1"/>
      <path d="M0,492C100,489 200,488 298,490V497H0Z" fill="var(--taupe)"/>
    </svg>
    <div class="camp-name"><span class="mark"></span>Walter Brisbane Fieldgrounds</div>

    <h2 class="level-title" style="left:18px;top:63px">DOLPHIN</h2>
    <div class="illo" role="img" aria-label="Illustration of a leaping dolphin" style="left:206px;top:57px;width:72px;height:70px"></div>
    <ul class="skills" style="left:26px;top:93px;width:180px;line-height:9.2px">
      <li style="margin-bottom:1.5px;width:200px">15 deep water bobs</li>
      <li style="margin-bottom:1.5px;width:200px">Correct body position and roll for backstroke</li>
      <li style="margin-bottom:1.5px">Basic whip kick on front</li>
      <li style="margin-bottom:1.5px">Basic elementary backstroke</li>
      <li style="margin-bottom:1.5px">Performs streamline position</li>
      <li style="margin-bottom:1.5px">Can reverse direction on front and back</li>
      <li style="margin-bottom:1.5px">Diving into deep end from standing position</li>
      <li>Assisted somersault from knees</li>
    </ul>
    <div class="move-up stacked" style="left:209px;top:129px;width:84px"><span class="move-up-tag">Move-Up</span><span>Must perform advanced backstroke with still head and side to side body roll consistently and with stamina</span></div>

    <h2 class="level-title" style="left:18px;top:234px">MARLIN</h2>
    <div class="illo" role="img" aria-label="Illustration of a leaping marlin" style="left:194px;top:214px;width:93px;height:88px"></div>
    <ul class="skills" style="left:26px;top:262px;width:200px;line-height:9.4px">
      <li style="width:170px">Proper elementary backstroke with timing and glide</li>
      <li>Proper whip kick on front and back</li>
      <li>Basic breaststroke arms</li>
      <li>Basic dolphin kick with body roll motion</li>
      <li>Basic sculling</li>
      <li>Open turns</li>
      <li style="width:150px">Somersault from wall or from standing position</li>
    </ul>
    <div class="move-up stacked" style="left:209px;top:312px;width:84px"><span class="move-up-tag">Move-Up</span><span>Must peform proper whip kick on front and back, and proper elementary backstroke.</span></div>

    <h2 class="level-title" style="left:18px;top:382px">BARRACUDA</h2>
    <div class="illo" role="img" aria-label="Illustration of a long barracuda" style="left:166px;top:401px;width:124px;height:25px"></div>
    <ul class="skills" style="left:26px;top:408px;width:165px;line-height:10px">
      <li>Proper breaststroke arms</li>
      <li>Proper breaststroke timing</li>
      <li>Basic sidestroke</li>
      <li>Standing dive</li>
      <li>Prone glide into summersault</li>
      <li>Dophin kick with streamline</li>
      <li>Sculling on front with flutter kick</li>
    </ul>
    <div class="move-up stacked" style="left:205px;top:432px;width:90px"><span class="move-up-tag">Move-Up</span><span>Must demonstrate full breaststroke with proper body/head positon with stamina</span></div>
  </section>

  <!-- Banner 5: Shark & Orca -->
  <section class="banner" style="left:589px;top:621px">
    <svg class="banner-shapes" viewBox="0 0 298 497" aria-hidden="true">
      <path d="M0,0H298V8C220,68 80,74 0,6Z" fill="var(--taupe)"/>
      <path d="M0,6C80,74 220,68 298,8" fill="none" stroke="var(--silver)" stroke-width="1.5"/>
      <path d="M0,284C110,300 230,262 298,212L298,262C230,282 110,300 0,326Z" fill="var(--taupe)"/>
      <path d="M0,284C110,300 230,262 298,212" fill="none" stroke="var(--silver)" stroke-width="1.5"/>
      <path d="M0,326C110,300 230,282 298,262" fill="none" stroke="var(--earth)" stroke-width="2"/>
      <path d="M85,497C130,482 200,480 250,497Z" fill="var(--taupe)"/>
    </svg>
    <div class="camp-name"><span class="mark"></span>Walter Brisbane Fieldgrounds</div>

    <h2 class="level-title" style="left:18px;top:86px">SHARK</h2>
    <div class="illo" role="img" aria-label="Illustration of a friendly shark" style="left:195px;top:81px;width:91px;height:56px"></div>
    <ul class="skills" style="left:30px;top:116px;width:240px;line-height:9.8px">
      <li style="margin-bottom:2.3px">Proper front crawl with stamina</li>
      <li style="margin-bottom:2.3px">Proper backstroke with stamina</li>
      <li style="margin-bottom:2.3px">Proper breaststroke with stamina</li>
      <li style="margin-bottom:2.3px">Proper elementary backstroke with stamina</li>
      <li style="margin-bottom:2.3px">Proper timing for sidestroke</li>
      <li style="margin-bottom:2.3px">Basic butterfly</li>
      <li style="margin-bottom:2.3px">Intro to flip turns</li>
      <li>Retrieve object from deep end and swim on back for 10 yards</li>
    </ul>
    <div class="move-up" style="left:16px;top:228px;align-items:center;gap:16px"><span class="move-up-tag">Move-Up</span><span>Must perform proper front<br>crawl, backstroke, and<br>breaststroke with stamina<br>and basic butterfly</span></div>

    <h2 class="level-title" style="left:18px;top:330px">ORCA</h2>
    <div class="illo" role="img" aria-label="Illustration of a leaping orca" style="left:201px;top:353px;width:82px;height:95px"></div>
    <ul class="skills" style="left:30px;top:360px;width:150px;line-height:9.8px">
      <li style="margin-bottom:2.3px">Demonstrate proficiency in all strokes for 50 yds</li>
      <li style="margin-bottom:2.3px">Proper butterfly</li>
      <li style="margin-bottom:2.3px">Front crawl flip turn</li>
      <li style="margin-bottom:2.3px">Backstroke flip turn</li>
      <li style="margin-bottom:2.3px">Open turns</li>
      <li>Shallow standing dive</li>
    </ul>
    <div class="move-up" style="left:16px;top:452px;align-items:center"><span class="move-up-tag">Move-Up</span><span>Must demonstrate proficiency in<br>all strokes and turns</span></div>
  </section>

</main>
</body>
</html>
```